Velitor creating new logo and business card design

Velitor is a consulting and business contribution for professional digital and real estate. We are specializing in lead generation / prospect want to invest in real estate that we connect with wealth manager or promoters. We identify prospects on all France, we call them and we put them in touch with professional able to meet their need. We wish to highlight our logo through the creation of value we bring to our customers. We provide them with contacts we obtained with tact, hence the solgan: tact in contact ... The logo should be created with the name Velitor. Playing with the name. If possible, put the slogan with the name and logo

Target Market(s)

Digital Immobiler

Industry/Entity Type

Digital

Contact Information for Business Card

RECTO :
Carvel Tiruan
CEO/Fondateur
Tel : 06 52 19 83 07
mail : tiruan.carvel@postelia.fr
VELITOR
14 rue des Orpailleurs
92340 Brevanne
VERSO : juste le logo

Logo Text

Velitor, le flair du lien

Font styles to use
Sans Serif
Decorative

Colors
ec1f27
e34297
85cae6
fbed22
f37122
9bcb3b
6b449b

Requirements
Must have
• We wish to have a logo that reflects our position as an innovative company and digital. The logo must be fluid, colorful and futuristic. We wish to highlight our logo through the creation of value we bring to our customers. We bring the contacts we have achieved tactfully, hence the solgan: tact in contact ...
Nice to have
• We like the Pluvex logo, toravine ... can bring out effect with a profile or target such I leave you free rein to your immagination
Should not have
• Nothing to report

```html
<!DOCTYPE html>
<html lang="fr">
<head>
<meta charset="utf-8">
<title>Velitor – carte de visite</title>
<link rel="stylesheet" href="https://fonts.googleapis.com/css2?family=Lato:wght@400;700;900&display=swap">
<style>
  :root {
    --bg: #eceef0;
    --card: #ffffff;
    --brand-blue: #0b5aa3;
    --ink: #2b2b2b;
    --white: #ffffff;
    --accent: #f37122;
    --shadow: rgba(0, 0, 0, 0.14);
  }
  * { box-sizing: border-box; margin: 0; padding: 0; }
  html, body {
    width: 1200px;
    height: 900px;
    overflow: hidden;
    background: var(--bg);
    font-family: "Lato", Arial, sans-serif;
  }
  .sheet {
    position: relative;
    width: 1200px;
    height: 900px;
  }
  .card {
    position: absolute;
    top: 282px;
    width: 520px;
    height: 336px;
    background: var(--card);
    box-shadow: 0 10px 26px var(--shadow), 0 2px 4px var(--shadow);
    overflow: hidden;
  }
  .card--front { left: 50px; }
  .card--back  { left: 630px; }

  .card__panel {
    position: absolute;
    inset: 0;
    width: 100%;
    height: 100%;
  }
  .card__panel polygon { fill: var(--brand-blue); }

  .brand {
    position: absolute;
    display: flex;
    align-items: center;
    gap: 10px;
    color: var(--brand-blue);
    font-weight: 900;
    letter-spacing: 2px;
  }
  .brand__dot {
    border-radius: 50%;
    background: var(--accent);
    flex: none;
  }
  .card--front .brand {
    left: 30px;
    top: 108px;
    font-size: 38px;
  }
  .card--front .brand__dot { width: 26px; height: 26px; }

  .holder {
    position: absolute;
    left: 150px;
    top: 196px;
    text-align: right;
    width: 150px;
  }
  .holder__name {
    font-size: 17px;
    color: var(--ink);
    font-weight: 400;
  }
  .holder__role {
    font-size: 12px;
    color: var(--brand-blue);
    margin-top: 2px;
  }

  .contact {
    position: absolute;
    left: 345px;
    top: 112px;
    list-style: none;
    color: var(--white);
    font-size: 13.5px;
    line-height: 1.35;
  }
  .contact__item {
    display: flex;
    align-items: flex-start;
    gap: 8px;
    margin-bottom: 3px;
  }
  .contact__icon {
    width: 11px;
    height: 14px;
    flex: none;
    margin-top: 2px;
  }
  .contact__icon * { fill: none; stroke: var(--white); stroke-width: 1.4; }
  .contact__icon .solid { fill: var(--white); stroke: none; }
  .contact__item--address { margin-top: 6px; }

  .card--back .brand {
    left: 0;
    right: 0;
    top: 0;
    bottom: 0;
    justify-content: center;
    font-size: 46px;
  }
  .card--back .brand__dot { width: 34px; height: 34px; }
</style>
</head>
<body>
<main class="sheet">

  <section class="card card--front" aria-label="Recto de la carte">
    <svg class="card__panel" viewBox="0 0 520 336" preserveAspectRatio="none" aria-hidden="true">
      <polygon points="300,0 520,0 520,336 360,336"/>
    </svg>

    <div class="brand">
      <span class="brand__dot"></span>
      <span class="brand__name">VELITOR</span>
    </div>

    <div class="holder">
      <p class="holder__name">Carvel Tiruan</p>
      <p class="holder__role">CEO/Fondateur</p>
    </div>

    <ul class="contact">
      <li class="contact__item">
        <svg class="contact__icon" viewBox="0 0 11 14" aria-hidden="true">
          <rect x="1.5" y="0.8" width="8" height="12.4" rx="1.5"/>
          <circle class="solid" cx="5.5" cy="11" r="0.9"/>
        </svg>
        <span>06 52 19 83 07</span>
      </li>
      <li class="contact__item">
        <svg class="contact__icon" viewBox="0 0 11 14" aria-hidden="true">
          <rect x="0.7" y="3.5" width="9.6" height="7" rx="0.8"/>
          <polyline points="0.9,4 5.5,7.8 10.1,4"/>
        </svg>
        <span>tiruan.carvel@postelia.fr</span>
      </li>
      <li class="contact__item contact__item--address">
        <svg class="contact__icon" viewBox="0 0 11 14" aria-hidden="true">
          <path d="M5.5 13 C2.5 9 1 7 1 5 A4.5 4.5 0 0 1 10 5 C10 7 8.5 9 5.5 13 Z"/>
          <circle class="solid" cx="5.5" cy="5" r="1.5"/>
        </svg>
        <span>14 rue des Orpailleurs<br>92340 Brevanne</span>
      </li>
    </ul>
  </section>

  <section class="card card--back" aria-label="Verso de la carte">
    <div class="brand">
      <span class="brand__dot"></span>
      <span class="brand__name">VELITOR</span>
    </div>
  </section>

</main>
</body>
</html>
```